Electric mountain bike tours nz

We are an Electric Mountain bike tour company in New Zealand. We will be offering bike rental and guided tours around the Nelson region in New Zealand. I want our website to represent both Mountain biking and New Zealand with the colours layout and features. We want tabs for the following:
-1 about us
-2 what we offer
-3 bookings/contact
Under the about us tab will be who we are as a a company. I want the ability to add videos to each of these tabs as we move foward with videos of the tracks we will be riding. I want the website to be editable so I can add and remove videos/photos myself. Also "our bikes" will be under this tab.
Under the what we offer tab will be
-1 bike rental and pricing
-2 guided tours and pricing
-3 recommended package deals.
I want to able to put the tracks under the guided tours tab and select beginner/ intermediate/advanced and have the tracks in each of the following to match the rider level. Also to be able to have a small video of the track would be great in this section.
Bookings and contact tab
(Further information for this tab to be updated soon)
- Silver ferns, kiwi, mountains

```html
<!DOCTYPE html>
<html lang="en">
<head>
<meta charset="utf-8">
<title>Kahu Ridge — Electric Mountain Biking</title>
<link href="https://fonts.googleapis.com/css2?family=Raleway:wght@300;400;500;600;700;800;900&display=swap" rel="stylesheet">
<style>
:root{
  --orange:#f05a22;
  --ink:#3b4443;
  --slate:#353d3c;
  --slate-btn:#5f6a68;
  --pale:#dfe4e3;
  --line:#8fa19e;
  --text:#4a4f4f;
  --footer:#23282b;
  --footer-deep:#1b1f21;
  --white:#ffffff;
}
*{box-sizing:border-box;margin:0;padding:0}
html,body{width:1200px;height:3169px;overflow:hidden}
body{position:relative;font-family:"Raleway",sans-serif;color:var(--text);background:var(--white)}
.abs{position:absolute}
.center{left:0;width:1200px;text-align:center}
.infinity{display:block;margin:0 auto;width:16px;height:8px}

/* hero */
.hero{left:0;top:0;width:1200px;height:606px;background:radial-gradient(ellipse at 50% 40%,#ffffff 0%,#f1f3f3 60%,#e3e7e6 100%)}
.hero-band{left:0;top:606px;width:1200px;height:311px;background:linear-gradient(180deg,#4f5a55 0%,#3c4642 55%,#2f3834 100%)}
.brand{left:169px;top:30px;display:flex;align-items:center;gap:10px;font-weight:800;font-size:22px;color:var(--ink);letter-spacing:1px}
.brand-dot{width:26px;height:26px;border-radius:50%;background:var(--ink)}
.nav{top:38px;left:672px;font-size:11.5px;font-weight:500;color:var(--ink)}
.nav a{position:absolute;white-space:nowrap;color:inherit;text-decoration:none}
.nav svg{position:absolute;left:22px;top:20px}
.hero-kicker{top:150px;font-size:17px;font-weight:700;letter-spacing:3px;color:var(--orange)}
.hero-title{top:160px;font-size:104px;font-weight:900;letter-spacing:14px;color:#48514f;line-height:1}
.hero-lede{top:262px;left:290px;width:620px;text-align:center;font-size:11px;line-height:17px}
.pill{display:inline-block;border-radius:18px;font-size:10px;font-weight:700;letter-spacing:1px;text-align:center;color:var(--white)}
.pill-orange{background:var(--orange)}
.pill-slate{background:var(--slate-btn)}
.pill-pale{background:var(--pale);color:var(--ink)}
.hero-cta{left:552px;top:309px;width:96px;height:32px;line-height:32px;z-index:3}
.slide-nav{top:294px;font-size:8px;letter-spacing:2px;color:#f3b9a3;display:flex;align-items:center;gap:6px}
.bike{left:300px;top:300px;width:566px;height:280px;z-index:2;background:radial-gradient(ellipse 48% 46% at 50% 55%,rgba(45,48,50,.85) 0%,rgba(70,74,76,.55) 60%,rgba(120,124,126,0) 100%)}

/* booking card */
.booking{left:173px;top:539px;width:856px;height:334px;background:var(--white);box-shadow:0 2px 8px rgba(0,0,0,.08)}
.booking h2{position:absolute;left:0;top:52px;width:100%;text-align:center;font-size:19px;font-weight:700;letter-spacing:3px;color:var(--ink)}
.booking .infinity{position:absolute;left:420px;top:78px}
.field{position:absolute;border:1px solid var(--line);font-size:8.5px;letter-spacing:1.2px;color:#99a5a3;padding:13px 12px}
.send{left:380px;top:241px;width:94px;height:34px;line-height:34px;position:absolute}

/* about */
.section-title{font-size:42px;font-weight:400;letter-spacing:6px;color:var(--ink)}
.section-sub{font-size:12px;letter-spacing:2px;color:#707978}
.section-lede{left:232px;width:740px;text-align:center;font-size:10.5px;line-height:16px}
.about-fade{left:0;top:1151px;width:516px;height:311px;background:linear-gradient(90deg,#e4e6e2 0%,#eef0ec 60%,#f6f7f5 100%)}
.media{overflow:hidden}
.play{position:absolute;left:50%;top:50%;width:46px;height:46px;margin:-23px 0 0 -23px;border:3px solid rgba(255,255,255,.8);border-radius:50%}
.play::after{content:"";position:absolute;left:16px;top:11px;border-left:15px solid rgba(255,255,255,.85);border-top:9px solid transparent;border-bottom:9px solid transparent}
.about-media{left:173px;top:1179px;width:417px;height:256px;background:linear-gradient(180deg,#2b4fb0 0%,#1d3a86 45%,#3f6b2a 75%,#1e2b12 100%)}
.about-copy{left:613px;top:1205px;width:405px;font-size:11.5px;line-height:17px}
.about-copy p+p{margin-top:15px}
.about-copy b{color:#262b2b;font-weight:600}
.about-btn{left:613px;top:1373px;width:116px;height:34px;line-height:34px}

/* offer */
.offer{left:0;top:1538px;width:1200px;height:674px;background:var(--slate)}
.offer-pre{top:1594px;font-size:22px;letter-spacing:4px;font-weight:400;color:var(--white)}
.offer-title{top:1612px;font-size:60px;letter-spacing:5px;font-weight:400;color:var(--white)}
.offer-lede{top:1688px;color:#b7bebd}
.card{position:absolute;top:1750px;width:271px}
.card .media{position:relative;height:243px}
.card h3{margin-top:22px;font-size:13.5px;font-weight:700;letter-spacing:1px;color:var(--white)}
.card p{margin-top:4px;font-size:11px;line-height:15px;color:#c9cfce}
.card .pill{margin-top:22px;width:118px;height:32px;line-height:32px}

/* contact */
.contact-field{position:absolute;border:1px solid var(--line);border-top:none}
.contact-field span{position:absolute;top:-6px;left:0;right:0;display:flex;align-items:center;font-size:8.5px;letter-spacing:1.3px;color:#6c7675}
.contact-field span::before{content:"";width:20px;border-top:1px solid var(--line);margin-right:8px}
.contact-field span::after{content:"";flex:1;border-top:1px solid var(--line);margin-left:8px}
.contact-send{left:532px;top:2667px;width:134px;height:38px;line-height:38px}

/* footer */
.footer{left:0;top:2791px;width:1200px;height:378px;background:var(--footer);border-top:4px solid var(--orange)}
.foot-col{position:absolute;top:2850px;width:300px;text-align:center;color:var(--white)}
.foot-col svg{display:block;margin:0 auto}
.foot-col h4{margin-top:12px;font-size:15px;font-weight:700;letter-spacing:4px;color:var(--white)}
.foot-col p{margin-top:14px;font-size:10px;letter-spacing:.5px;color:#d4d8d9}
.social{left:540px;top:3002px;display:flex;gap:6px}
.social span{width:36px;height:36px;border:1.5px solid #c9cdce;border-radius:3px}
.foot-nav{top:3060px;left:0;width:1200px;display:flex;justify-content:center;gap:42px;font-size:9.5px;letter-spacing:1px;color:#c9cdce}
.copyright{left:0;top:3123px;width:1200px;height:46px;line-height:46px;background:var(--footer-deep);text-align:center;font-size:8.5px;letter-spacing:1px;color:#b9bfc0}
</style>
</head>
<body>
<svg width="0" height="0" style="position:absolute">
  <symbol id="inf" viewBox="0 0 16 8"><path d="M8 4C6 1 2 1 2 4s4 3 6 0 6-3 6 0-4 3-6 0z" fill="none" stroke="currentColor" stroke-width="1.6"/></symbol>
</svg>

<!-- Hero -->
<div class="abs hero"></div>
<div class="abs hero-band" role="img" aria-label="Dark forest trail photograph"></div>

<div class="abs brand"><span class="brand-dot"></span>Kahu Ridge</div>
<nav class="abs nav">
  <a style="left:0">ABOUT US</a>
  <svg width="16" height="8" style="color:var(--ink)"><use href="#inf"/></svg>
  <a style="left:101px">WHAT WE OFFER</a>
  <a style="left:239px">BOOKINGS/CONTACT</a>
</nav>

<div class="abs center hero-kicker">ELECTRIC MOUNTAIN</div>
<h1 class="abs center hero-title">BIKING</h1>
<p class="abs hero-lede">Lorem ipsum dolor sit amet, consectetur adipiscing elit. Nam eget tincidunt lacus. Nulla facilisi. Sed a nibh non odio varius blandit. Nullam vulputate velit ante, eu cursus nulla porttitor.</p>

<div class="abs slide-nav" style="left:80px">PREVIOUS <svg width="12" height="18"><path d="M10 2L3 9l7 7" fill="none" stroke="#f3a585" stroke-width="3"/></svg></div>
<div class="abs slide-nav" style="left:1040px"><svg width="12" height="18"><path d="M2 2l7 7-7 7" fill="none" stroke="#b7bcbc" stroke-width="3"/></svg> NEXT</div>

<!-- Booking card -->
<section class="abs booking">
  <h2>BOOK YOUR BIKE</h2>
  <svg class="infinity" style="color:var(--ink)"><use href="#inf"/></svg>
  <div class="field" style="left:74px;top:110px;width:231px;height:38px">NAME AND SURNAME</div>
  <div class="field" style="left:313px;top:110px;width:230px;height:38px">EMAIL</div>
  <div class="field" style="left:552px;top:110px;width:230px;height:38px">PHONE NUMBER</div>
  <div class="field" style="left:74px;top:160px;width:708px;height:57px">ADDITIONAL NOTES</div>
  <span class="pill pill-slate send">SEND</span>
</section>
<div class="abs bike" role="img" aria-label="Black electric mountain bike, side view"></div>
<span class="abs pill pill-orange hero-cta">CLICK HERE</span>

<!-- About -->
<h2 class="abs center section-title" style="top:975px">ABOUT US</h2>
<div class="abs center section-sub" style="top:1028px">WHO WE ARE</div>
<svg class="abs" style="left:592px;top:1046px;width:16px;height:8px;color:var(--ink)"><use href="#inf"/></svg>
<p class="abs section-lede" style="top:1068px">Lorem ipsum dolor sit amet, consectetur adipiscing elit. Nam eget tincidunt lacus. Nulla facilisi. Sed a nibh non odio varius blandit. Nullam vulputate velit ante, eu cursus nulla porttitor ut. Vestibulum efficitur accumsan tellus in eleifend.</p>

<div class="abs about-fade" role="img" aria-label="Faded forest trail photograph"></div>
<div class="abs media about-media" role="img" aria-label="Video: electric mountain bike on a ridge above the bay"><span class="play"></span></div>
<div class="abs about-copy">
  <p>Lorem ipsum dolor sit amet, <b>consectetur adipiscing elit</b>. Nam eget tincidunt lacus. Nulla facilisi. Sed a nibh non odio varius blandit. Nullam vulputate velit ante, eu cursus nulla porttitor ut. Vestibulum efficitur accumsan tellus in eleifend.</p>
  <p>Phasellus imperdiet, nulla id fringilla pulvinar Lorem ipsum dolor sit amet, consectetur adipiscing elit. Nam eget tincidunt lacus. Nulla facilisi. Sed a nibh non odio varius blandit. Nullam vulputate velit ante.</p>
</div>
<span class="abs pill pill-orange about-btn">LEARN MORE</span>

<!-- What we offer -->
<section class="abs offer"></section>
<div class="abs center offer-pre">WHAT WE</div>
<h2 class="abs center offer-title">OFFER</h2>
<svg class="abs" style="left:592px;top:1680px;width:16px;height:8px;color:var(--white)"><use href="#inf"/></svg>
<p class="abs section-lede offer-lede" style="top:1692px">Lorem ipsum dolor sit amet, consectetur adipiscing elit. Nam eget tincidunt lacus. Nulla facilisi. Sed a nibh non odio varius blandit. Nullam vulputate velit ante, eu cursus nulla porttitor ut. Vestibulum efficitur accumsan tellus in eleifend.</p>

<article class="card" style="left:173px">
  <div class="media" role="img" aria-label="Video: rental bike beside a forest trail sign" style="background:linear-gradient(160deg,#b5622f 0%,#6f4a2a 45%,#3d5a2c 100%)"><span class="play"></span></div>
  <h3>BIKE RENTAL AND PRICING</h3>
  <p>Lorem ipsum dolor sit amet, consectetur adipiscing elit. Nam eget tincidunt lacus Nulla facilisi. Sed a nibh non odio varius blandit.</p>
  <span class="pill pill-orange">LEARN MORE</span>
</article>
<article class="card" style="left:465px">
  <div class="media" role="img" aria-label="Video: guided tour bike on a hilltop" style="background:linear-gradient(180deg,#2b4fb0 0%,#1d3a86 45%,#3f6b2a 75%,#1e2b12 100%)"><span class="play"></span></div>
  <h3>GUIDED TOURS AND PRICING</h3>
  <p>Lorem ipsum dolor sit amet, consectetur adipiscing elit. Nam eget tincidunt lacus Nulla facilisi. Sed a nibh non odio varius blandit.</p>
  <span class="pill pill-pale">LEARN MORE</span>
</article>
<article class="card" style="left:758px">
  <div class="media" role="img" aria-label="Video: bike parked by pine trees overlooking the coast" style="background:linear-gradient(180deg,#3d7fd0 0%,#7fa9d4 40%,#2f4a26 70%,#1b2515 100%)"><span class="play"></span></div>
  <h3>RECOMMENDED PACKAGE DEALS</h3>
  <p>Lorem ipsum dolor sit amet, consectetur adipiscing elit. Nam eget tincidunt lacus Nulla facilisi. Sed a nibh non odio varius blandit.</p>
  <span class="pill pill-pale">LEARN MORE</span>
</article>

<!-- Contact -->
<h2 class="abs center section-title" style="top:2274px">CONTACT</h2>
<div class="abs center section-sub" style="top:2328px;font-size:11px">WRITE US YOUR MESSAGE</div>
<svg class="abs" style="left:592px;top:2349px;width:16px;height:8px;color:var(--ink)"><use href="#inf"/></svg>

<div class="contact-field" style="left:173px;top:2400px;width:417px;height:45px"><span>ENTER YOUR NAME</span></div>
<div class="contact-field" style="left:613px;top:2400px;width:418px;height:45px"><span>ENTER YOUR EMAIL</span></div>
<div class="contact-field" style="left:173px;top:2470px;width:417px;height:45px"><span>ENTER YOUR PHONE NO</span></div>
<div class="contact-field" style="left:613px;top:2470px;width:418px;height:45px"><span>YOUR MESSAGE SUBJECT</span></div>
<div class="contact-field" style="left:173px;top:2538px;width:858px;height:91px"><span>ENTER YOUR MESSAGE</span></div>
<span class="abs pill pill-slate contact-send">SEND MESSAGE</span>

<!-- Footer -->
<footer class="abs footer"></footer>
<div class="foot-col" style="left:158px">
  <svg width="22" height="30" viewBox="0 0 22 30"><path d="M11 1C5.5 1 1.5 5 1.5 10.5 1.5 18 11 29 11 29s9.5-11 9.5-18.5C20.5 5 16.5 1 11 1z" fill="none" stroke="#fff" stroke-width="2"/><circle cx="11" cy="10.5" r="3.5" fill="#fff"/></svg>
  <h4>LOCATION</h4>
  <p>48 MATAI LANE , NELSON</p>
</div>
<div class="foot-col" style="left:452px">
  <svg width="30" height="30" viewBox="0 0 30 30"><path d="M7 3l5 6-3 3c1.5 3.5 4.5 6.5 8 8l3-3 6 5-3 4C13 26 4 17 3 7z" fill="none" stroke="#fff" stroke-width="1.8" stroke-linejoin="round"/><path d="M17 8a6 6 0 0 1 5 5M17 3a11 11 0 0 1 10 10" fill="none" stroke="#fff" stroke-width="1.6"/></svg>
  <h4>PHONE</h4>
  <p>1-000-555-0142</p>
</div>
<div class="foot-col" style="left:742px">
  <svg width="30" height="30" viewBox="0 0 30 30"><rect x="3" y="6" width="24" height="18" fill="none" stroke="#fff" stroke-width="1.8"/><path d="M3 6l12 10 12-10M3 24l9-8M27 24l-9-8" fill="none" stroke="#fff" stroke-width="1.6"/></svg>
  <h4>EMAIL</h4>
  <p>HELLO@KAHURIDGE.EXAMPLE</p>
</div>
<div class="abs" style="left:0;top:2975px;width:1200px;border-top:1px solid #2e3437"></div>
<div class="abs social" aria-label="Social links"><span></span><span></span><span></span></div>
<div class="abs foot-nav"><span>ABOUT US</span><span>WHAT WE OFFER</span><span>BOOKINGS/CONTACT</span></div>
<div class="abs copyright">COPYRIGHT 2018. ALL RIGHT RESERVED</div>
</body>
</html>
```